Design some Business Cards for Tail Buddy

Hi There,

After some business cards for a business that does dog walking, at home pet visits and pet day care.

Attached is the logo in both PNG and PSD format. Design should be simple and clean, with a white background both on the front and the back. Logo should be on the front and the following on the back:

Mara Fenwick
Dog Walking At Home Pet Visits Pet Day Care
0411573826

Looking forward to your designs!
Thanks

```html
<!DOCTYPE html>
<html lang="en">
<head>
<meta charset="utf-8">
<title>Tail Buddy – Business Cards</title>
<link rel="stylesheet" href="https://fonts.googleapis.com/css2?family=Open+Sans:wdth,wght@75,300&family=Oswald:wght@600&display=swap">
<style>
  :root {
    --stage: #e6e8eb;
    --card: #ffffff;
    --ink: #161616;
    --brand-blue: #1f6fe0;
    --card-shadow: rgba(0, 0, 0, 0.14);
  }
  * { margin: 0; padding: 0; box-sizing: border-box; }
  html, body {
    width: 1200px;
    height: 829px;
    overflow: hidden;
    background: var(--stage);
  }
  .card-set {
    position: relative;
    width: 1200px;
    height: 829px;
  }
  .card {
    position: absolute;
    top: 266px;
    width: 520px;
    height: 297px;
    background: var(--card);
    border-radius: 14px;
    box-shadow: 0 10px 30px var(--card-shadow);
    overflow: hidden;
  }
  .card--front { left: 60px; }
  .card--back { left: 620px; }

  .brand-word {
    font-family: "Open Sans", "Arial Narrow", sans-serif;
    font-weight: 300;
    font-stretch: 75%;
    color: var(--ink);
    line-height: 1;
    white-space: nowrap;
  }
  .brand-dot {
    border-radius: 50%;
    background: var(--brand-blue);
  }

  /* Front */
  .front-brand {
    position: absolute;
    left: 0;
    top: 36px;
    width: 100%;
    display: flex;
    flex-direction: column;
    align-items: center;
  }
  .front-brand .brand-dot {
    width: 104px;
    height: 104px;
  }
  .front-brand .brand-word {
    margin-top: 12px;
    font-size: 104px;
  }

  /* Back */
  .contact {
    position: absolute;
    left: 36px;
    top: 30px;
    width: 260px;
    text-align: center;
    font-family: "Oswald", Impact, sans-serif;
    font-weight: 600;
    color: var(--ink);
    font-size: 17px;
    line-height: 1.5;
  }
  .back-brand {
    position: absolute;
    right: 34px;
    bottom: 30px;
    display: flex;
    flex-direction: column;
    align-items: flex-end;
  }
  .back-brand .brand-dot {
    width: 54px;
    height: 54px;
    margin-right: 44px;
  }
  .back-brand .brand-word {
    margin-top: 10px;
    font-size: 44px;
  }
</style>
</head>
<body>
  <main class="card-set">
    <section class="card card--front" aria-label="Card front">
      <div class="front-brand">
        <span class="brand-dot" aria-hidden="true"></span>
        <span class="brand-word">Tail Buddy</span>
      </div>
    </section>

    <section class="card card--back" aria-label="Card back">
      <div class="contact">
        <p class="contact-name">Mara Fenwick</p>
        <p>Dog Walking</p>
        <p>At Home Pet Visits Pet Day Care</p>
        <p class="phone">0411573826</p>
      </div>
      <div class="back-brand">
        <span class="brand-dot" aria-hidden="true"></span>
        <span class="brand-word">Tail Buddy</span>
      </div>
    </section>
  </main>
</body>
</html>
```